Business Card Design Project

We consult with hotels on setting rates and maximizing a revenue strategy

Industry/Entity Type

Business

Contact Information for Business Card

I am not sure what I want. Our company offers high level consulting to hotels around the country but we are also laid back. I would like something that is professional but also shows the laid back side

```html
<!DOCTYPE html>
<html lang="en">
<head>
<meta charset="utf-8">
<title>Crestway Business Card</title>
<link href="https://fonts.googleapis.com/css2?family=Gelasio:wght@400&family=Open+Sans:wght@400;600;700&display=swap" rel="stylesheet">
<style>
  :root {
    --navy: #2c3550;
    --tan: #cdb57e;
    --paper: #f7f7f5;
    --ink: #1e1e1e;
    --muted: #6b6b6b;
    --icon: #8a8a8a;
    --backdrop: #e6e3de;
  }
  * { margin: 0; padding: 0; box-sizing: border-box; }
  html, body { width: 1200px; height: 1000px; overflow: hidden; }
  body { background: var(--backdrop); position: relative; font-family: "Open Sans", sans-serif; }

  .card { position: absolute; width: 412px; height: 290px; box-shadow: 0 2px 6px rgba(0,0,0,.18); overflow: hidden; }

  /* Back of card */
  .card-back { left: 452px; top: 128px; background: var(--navy); }
  .card-back .band { position: absolute; left: 0; right: 0; top: 96px; height: 95px; background: var(--tan);
    display: flex; flex-direction: column; align-items: center; justify-content: center; gap: 4px; }
  .brand { display: flex; align-items: center; gap: 6px; font-family: "Open Sans", sans-serif; font-weight: 700;
    color: var(--ink); letter-spacing: .5px; }
  .brand-mark { width: 10px; height: 10px; background: var(--navy); }
  .card-back .brand { font-size: 16px; }
  .back-web { font-size: 8px; font-weight: 600; color: var(--ink); }

  /* Front of card */
  .card-front { left: 280px; top: 515px; background: var(--paper); }
  .front-shape { position: absolute; inset: 0; }
  .card-front .brand { position: absolute; left: 256px; top: 158px; font-size: 15px; }
  .person { position: absolute; left: 30px; top: 112px; }
  .person-name { font-family: "Gelasio", serif; font-size: 18px; color: var(--ink); }
  .person-title { font-size: 10px; color: var(--muted); margin-top: 6px; }
  .contacts { position: absolute; left: 30px; top: 182px; list-style: none; }
  .contacts li { display: flex; align-items: center; gap: 8px; height: 20px; font-size: 10.5px;
    color: var(--muted); letter-spacing: .6px; }
  .contacts svg { width: 12px; height: 12px; flex: none; }
</style>
</head>
<body>

<section class="card card-back" aria-label="Card back">
  <div class="band">
    <div class="brand"><span class="brand-mark"></span>CRESTWAY</div>
    <div class="back-web">www.CrestwayRMS.com</div>
  </div>
</section>

<section class="card card-front" aria-label="Card front">
  <svg class="front-shape" viewBox="0 0 412 290" aria-hidden="true">
    <path d="M388 0 C262 40 192 140 190 290 L412 290 L412 0 Z" fill="var(--tan)"/>
    <path d="M396 0 C264 38 184 140 182 290" fill="none" stroke="var(--navy)" stroke-width="2.5"/>
  </svg>

  <div class="brand"><span class="brand-mark"></span>CRESTWAY</div>

  <div class="person">
    <div class="person-name">Dana Whitfield</div>
    <div class="person-title">Regional Revenue Manager</div>
  </div>

  <ul class="contacts">
    <li>
      <svg viewBox="0 0 12 12"><circle cx="6" cy="6" r="6" fill="#dcdcdc"/><rect x="4.2" y="2.5" width="3.6" height="7" rx=".8" fill="var(--icon)"/></svg>
      555-014-2290
    </li>
    <li>
      <svg viewBox="0 0 12 12"><circle cx="6" cy="6" r="6" fill="#dcdcdc"/><rect x="3" y="4.5" width="6" height="3.5" rx=".5" fill="var(--icon)"/><rect x="4" y="2.5" width="4" height="2" fill="var(--icon)"/><rect x="4" y="8" width="4" height="1.5" fill="var(--icon)"/></svg>
      555-014-7731
    </li>
    <li>
      <svg viewBox="0 0 12 12"><circle cx="6" cy="6" r="6" fill="#dcdcdc"/><rect x="3" y="3.8" width="6" height="4.4" fill="none" stroke="var(--icon)" stroke-width=".9"/><path d="M3 3.8 L6 6.3 L9 3.8" fill="none" stroke="var(--icon)" stroke-width=".9"/></svg>
      Dana@CrestwayRMS.com
    </li>
    <li>
      <svg viewBox="0 0 12 12"><circle cx="6" cy="6" r="6" fill="#dcdcdc"/><circle cx="6" cy="6" r="3" fill="none" stroke="var(--icon)" stroke-width=".9"/><path d="M3 6 H9 M6 3 V9" stroke="var(--icon)" stroke-width=".7"/></svg>
      www.CrestwayRMS.com
    </li>
  </ul>
</section>

</body>
</html>
```